Business Card Design

We are a full service general contractor that specializes in emergency services and insurance restoration/repair. Most of our work relates to water damage, fire dame, smoke, wind and hail, storm damage, etc. Pretty much anything you would call your insurance company for.

On one side of card the logo is VERY easy with the possibility of some modifications once I get a preview. I had a logo designed years ago and its on all my vehicles so I want to stick with my branding at this point and time.

Its a 2 sided card-for one side I would like the following:
* See logo (its attached)
* I would like this logo as large/big/bold as possible-essentially it should fill up the entire side of the card (barring it not looking proportionally correct of course)
* I think the background should be white behind it-or possibly red (with colors inverted so that they don't get lost in the red background)
* I'm attaching a photo of one of our work vans to go off of-you will notice that the .com wraps up the side of the logo-this .com portion needs to added on as the logo is only the kestrel restoration logo

The other side of the card I'm thinking should be:
* My biggest struggle is formatting-in other words-I don't know how to lay out all that info without the card looking jumbled/messy
* all our logos, vehicles, marketing media, etc. is based on or at least inspired by a clean look
* a smaller version of logo (without the .com) should be located somewhere on this side of card-I've seen some cards where its centered and others where its offset-I'm not sure which is better
* I could conceivably leave off PO BOX if its too much info and something needs deleted

Business

The logo will display company name-other pertinent info:
Phone: 704 555 0182
Mobile: 704 555 0147
Fax: 704 555 0163
email: kestrelrestoration@mailnest-example.com
Address: 2958 Willow Rd.
Harlow Springs, OR
PO BOX 60357 97405

```html
<!DOCTYPE html>
<html lang="en">
<head>
<meta charset="utf-8">
<title>Kestrel Restoration — Business Card</title>
<link rel="stylesheet" href="https://fonts.googleapis.com/css2?family=Open+Sans:wght@400;700;800&display=swap">
<style>
  :root {
    --backdrop: #2b2b2d;
    --slate: #3f5869;
    --white: #ffffff;
    --red: #c0141c;
    --grey: #5b6670;
    --rule-light: rgba(255,255,255,0.85);
  }
  * { margin: 0; padding: 0; box-sizing: border-box; }
  html, body { width: 1200px; height: 900px; overflow: hidden; }
  body { background: var(--backdrop); font-family: "Open Sans", sans-serif; position: relative; }

  .card { position: absolute; width: 680px; height: 390px; overflow: hidden; box-shadow: 0 14px 30px rgba(0,0,0,0.45); }
  .card-front { left: 80px; top: 50px; background: var(--slate); }
  .card-back { left: 440px; top: 470px; background: var(--white); }

  .frame { position: absolute; inset: 0; width: 100%; height: 100%; }

  .front-name {
    position: absolute; left: 0; right: 0; top: 170px;
    text-align: center; color: var(--white);
    font-weight: 800; font-size: 40px; line-height: 1.2; letter-spacing: 0.5px;
  }

  .back-name {
    position: absolute; left: 60px; top: 150px;
    color: var(--slate); font-weight: 800; font-size: 26px; line-height: 1.2;
  }

  .person { position: absolute; right: 62px; top: 100px; text-align: right; }
  .person-name { color: var(--red); font-weight: 700; font-size: 24px; letter-spacing: 0.5px; padding-bottom: 3px; border-bottom: 1px solid var(--grey); }
  .person-role { color: var(--grey); font-size: 12px; letter-spacing: 1px; margin-top: 2px; }

  .address { position: absolute; right: 62px; top: 190px; text-align: right; color: var(--grey); font-size: 14px; line-height: 1.4; }

  .contacts { position: absolute; left: 40px; top: 268px; width: 330px; border-top: 1px solid var(--red); padding-top: 8px; list-style: none; }
  .contacts li { display: flex; align-items: center; gap: 8px; color: var(--grey); font-size: 14px; line-height: 1.45; }
  .contacts svg { width: 12px; height: 12px; fill: var(--red); flex: none; }
</style>
</head>
<body>

<section class="card card-front" aria-label="Card front">
  <svg class="frame" viewBox="0 0 680 390" aria-hidden="true">
    <g stroke="var(--rule-light)" stroke-width="1.2">
      <line x1="0" y1="18" x2="680" y2="18"/>
      <line x1="0" y1="372" x2="680" y2="372"/>
      <line x1="18" y1="0" x2="18" y2="390"/>
      <line x1="662" y1="0" x2="662" y2="390"/>
    </g>
  </svg>
  <p class="front-name">kestrelrestoration.com</p>
</section>

<section class="card card-back" aria-label="Card back">
  <svg class="frame" viewBox="0 0 680 390" aria-hidden="true">
    <g stroke="var(--red)" stroke-width="1.2">
      <line x1="0" y1="18" x2="680" y2="18"/>
      <line x1="0" y1="372" x2="680" y2="372"/>
      <line x1="18" y1="0" x2="18" y2="390"/>
      <line x1="662" y1="0" x2="662" y2="390"/>
    </g>
  </svg>

  <p class="back-name">Kestrel Restoration</p>

  <div class="person">
    <p class="person-name">DALE CORRIGAN</p>
    <p class="person-role">DIRECTOR</p>
  </div>

  <p class="address">2958 Willow Rd. Harlow Springs<br>OR PO BOX 60357 97405</p>

  <ul class="contacts">
    <li><svg viewBox="0 0 24 24"><path d="M6.6 10.8a15 15 0 0 0 6.6 6.6l2.2-2.2a1 1 0 0 1 1-.25 11.4 11.4 0 0 0 3.6.6 1 1 0 0 1 1 1V20a1 1 0 0 1-1 1A17 17 0 0 1 3 4a1 1 0 0 1 1-1h3.5a1 1 0 0 1 1 1c0 1.25.2 2.45.6 3.6a1 1 0 0 1-.25 1z"/></svg>704 555 0182</li>
    <li><svg viewBox="0 0 24 24"><path d="M7 1h10a2 2 0 0 1 2 2v18a2 2 0 0 1-2 2H7a2 2 0 0 1-2-2V3a2 2 0 0 1 2-2zm0 3v14h10V4zm5 15.5a1.2 1.2 0 1 0 0 2.4 1.2 1.2 0 0 0 0-2.4z"/></svg>704 555 0147</li>
    <li><svg viewBox="0 0 24 24"><path d="M6 2h12v6H6zM3 9h18a2 2 0 0 1 2 2v7h-4v4H5v-4H1v-7a2 2 0 0 1 2-2zm4 7v4h10v-4z"/></svg>704 555 0163</li>
    <li><svg viewBox="0 0 24 24"><path d="M2 4h20a1 1 0 0 1 1 1v14a1 1 0 0 1-1 1H2a1 1 0 0 1-1-1V5a1 1 0 0 1 1-1zm1 3v11h18V7l-9 6z"/></svg>kestrelrestoration@mailnest-example.com</li>
  </ul>
</section>

</body>
</html>
```